Breast Cancer Banner/Flyer

This flyer/Banner 2.75ft x 6.75ft is a Do it Yourself infographic on how to to self breast exams. see attached examples.
Please add sponsor logos at the bottom and walk with willow logo at the top
Please add Breast Cancer Ribbon

```html
<!DOCTYPE html>
<html lang="en">
<head>
<meta charset="utf-8">
<title>Breast Self Exam – Walk with Willow</title>
<link rel="stylesheet" href="https://fonts.googleapis.com/css2?family=Archivo+Black&family=Roboto+Condensed:ital,wght@0,400;0,700;1,800;1,900&family=Playfair+Display:ital,wght@1,800&display=swap">
<style>
  :root{
    --magenta:#ff1493;
    --magenta-deep:#e6007e;
    --wine:#8a003f;
    --wine-dark:#2b0012;
    --rose:#f7a8d0;
    --blush:#fbd3ea;
    --blush-light:#fff0f8;
    --ink:#1a1a1a;
    --white:#ffffff;
  }
  *{margin:0;padding:0;box-sizing:border-box}
  html,body{width:1200px;height:2507px;overflow:hidden;background:var(--white)}
  .banner{position:relative;width:1200px;height:2507px;overflow:hidden;font-family:"Roboto Condensed",sans-serif;color:var(--ink)}

  .hero{position:absolute;left:0;top:0;width:1200px;height:803px;
    background:
      radial-gradient(ellipse 900px 700px at 100% 0%, #d6006a 0%, rgba(214,0,106,0) 70%),
      linear-gradient(200deg,#a8004e 0%,#7a0036 45%,var(--wine-dark) 100%);}
  .brand{position:absolute;left:0;top:60px;width:1200px;text-align:center}
  .brand-mark{display:block;width:190px;height:190px;margin:0 auto;border-radius:50%;background:var(--blush);border:8px solid var(--rose)}
  .brand-name{display:block;margin-top:26px;font-weight:700;font-size:44px;color:var(--white);letter-spacing:1px}
  .brand-sub{position:absolute;left:0;top:400px;width:1200px;text-align:center;font-weight:700;font-size:27px;color:var(--white);letter-spacing:.5px}

  .ribbon-art{position:absolute;left:110px;top:455px;width:555px;height:318px;border-radius:40px;
    background:linear-gradient(35deg,#d1005f 0%,#f06aa8 45%,#fbd3ea 100%);opacity:.9}

  .headline{position:absolute;left:520px;top:505px;width:660px;font-style:italic;font-weight:900;line-height:1;letter-spacing:-2px}
  .headline .line-1{display:block;margin-left:170px;font-size:128px;color:var(--white)}
  .headline .line-2{display:block;margin-top:-6px;font-size:136px;color:var(--rose);text-shadow:4px 6px 8px rgba(0,0,0,.35)}

  .exam-band{position:absolute;left:0;top:803px;width:1200px;height:78px;background:var(--magenta-deep);
    text-align:center;font-family:"Archivo Black",sans-serif;font-size:58px;line-height:78px;color:var(--white);letter-spacing:4px}

  .steps{position:absolute;left:0;top:881px;width:1200px;height:1130px;
    background:radial-gradient(ellipse 700px 600px at 60% 45%, var(--blush-light) 0%, var(--blush) 100%)}

  .step{position:absolute;left:75px;width:1110px}
  .step-art{position:absolute;left:0;top:0;width:316px;height:305px;border:11px solid var(--magenta-deep);border-radius:22px;background:#f4d6b5}
  .step-art.shower{background:linear-gradient(135deg,#fbeee0 0%,#e9a877 60%,#c77a4c 100%)}
  .step-art.mirror{background:linear-gradient(160deg,#f7e8d6 0%,#e09a6c 55%,#8a5030 100%)}
  .step-art.lying{background:linear-gradient(150deg,#f3e6cf 0%,#c98157 50%,#5e3a28 100%)}
  .step-text{position:absolute;left:337px;top:42px;width:760px}
  .step-title{font-weight:700;font-size:44px;color:var(--magenta-deep);line-height:1.1;margin-bottom:8px}
  .step-body{font-size:31px;line-height:35px;font-weight:400}
  .step-list{list-style:none;font-size:31px;line-height:35px}
  .step-list li{position:relative;padding-left:24px}
  .step-list li::before{content:"•";position:absolute;left:0;top:0}

  .step-1{top:31px}
  .step-2{top:375px}
  .step-2 .step-text{left:345px;top:30px}
  .step-3{top:742px}
  .step-3 .step-text{top:16px}

  .wave{position:absolute;left:0;top:1975px;width:1200px;height:70px}

  .sponsors{position:absolute;left:0;top:2045px;width:1200px;height:335px;background:var(--white)}
  .sponsor{position:absolute;transform:translate(-50%,-50%);white-space:nowrap;font-weight:700;font-size:27px;display:flex;align-items:center;gap:10px}
  .sponsor .dot{width:22px;height:22px;border-radius:50%}
  .s-clearpeak{left:195px;top:106px;color:#1f4fa3}
  .s-sunrise{left:449px;top:106px;color:#1a2a4a}
  .s-palm{left:703px;top:106px;color:#111}
  .s-tideline{left:985px;top:106px;color:#2e4d66}
  .s-highbrook{left:182px;top:250px;color:#1f64b5}
  .s-vitalcrest{left:485px;top:250px;color:#c0272d}
  .s-zestgrove{left:751px;top:250px;color:#6a2c8c}
  .s-wellmark{left:977px;top:250px;color:#2a6db5}

  .tagline-band{position:absolute;left:0;top:2384px;width:1200px;height:123px;background:var(--magenta-deep);
    border-top:6px solid #f9c7e2;text-align:center}
  .tagline{font-family:"Playfair Display",serif;font-style:italic;font-weight:800;font-size:50px;line-height:100px;color:var(--white)}
</style>
</head>
<body>
<div class="banner">

  <header class="hero">
    <div class="brand">
      <span class="brand-mark"></span>
      <span class="brand-name">Walk with Willow</span>
    </div>
    <p class="brand-sub">BREAST CANCER SUPPORT GROUP</p>
    <div class="ribbon-art" role="img" aria-label="Pink awareness ribbon flowing into a rising mosaic arrow"></div>
    <h1 class="headline"><span class="line-1">Do It</span><span class="line-2">Yourself!</span></h1>
  </header>

  <h2 class="exam-band">BREAST SELF EXAM</h2>

  <section class="steps">
    <article class="step step-1">
      <div class="step-art shower" role="img" aria-label="Woman in the shower checking her breast with circular fingertip motions"></div>
      <div class="step-text">
        <h3 class="step-title">IN THE SHOWER</h3>
        <p class="step-body">Beginning at the armpit and<br>continuing inwards,<br>move your fingertips around your<br>entire breast in a circular motion<br>and feel for any lump or thickening.</p>
      </div>
    </article>

    <article class="step step-2">
      <div class="step-art mirror" role="img" aria-label="Woman standing with hands on hips examining her breasts in a mirror"></div>
      <div class="step-text">
        <h3 class="step-title">IN THE FRONT OF A MIRROR</h3>
        <ul class="step-list">
          <li>Place hands on hips.</li>
          <li>Look for changes in size, shape skin texture<br>and squeeze nipples for signs of discharge.</li>
          <li>Lean forward and examine each breast<br>for dimpling of the skin or nipples that<br>are depressed inward.</li>
        </ul>
      </div>
    </article>

    <article class="step step-3">
      <div class="step-art lying" role="img" aria-label="Woman lying down pressing her breast in a circular motion"></div>
      <div class="step-text">
        <h3 class="step-title">LYING DOWN</h3>
        <ul class="step-list">
          <li>Use the flat of your hand and keep your fingers<br>straight and close together to gently but firmly<br>press the breast in a circular motion, moving<br>inwards from the armpit to the nipple.</li>
          <li>Feel for lumps along the collarbone and in the armpit.</li>
          <li>If you detect any lumps or changes in the breast,<br>consult a medical professional as soon as possible.</li>
        </ul>
      </div>
    </article>
  </section>

  <svg class="wave" viewBox="0 0 1200 70" preserveAspectRatio="none" aria-hidden="true">
    <path d="M0 0 H1200 V25 C900 -5 600 10 300 55 C180 72 80 65 0 45 Z" fill="#fbd3ea"/>
    <path d="M0 45 C80 65 180 72 300 55 C600 10 900 -5 1200 25 V42 C900 15 600 30 300 68 C180 80 80 75 0 55 Z" fill="#e6007e"/>
    <path d="M0 55 C80 75 180 80 300 68 C600 30 900 15 1200 42 V70 H0 Z" fill="#ffffff"/>
  </svg>

  <section class="sponsors" aria-label="Sponsors">
    <div class="sponsor s-clearpeak">Clearpeak Water</div>
    <div class="sponsor s-sunrise"><span class="dot" style="background:#8cc63f"></span>Sunrise Apothecary</div>
    <div class="sponsor s-palm">Palm Isle Apparel</div>
    <div class="sponsor s-tideline">Tideline Bar</div>
    <div class="sponsor s-highbrook">Highbrook Springs</div>
    <div class="sponsor s-vitalcrest">Vitalcrest Medical</div>
    <div class="sponsor s-zestgrove"><span class="dot" style="background:#f5a623"></span>Zestgrove</div>
    <div class="sponsor s-wellmark">Wellmark Pharmacy</div>
  </section>

  <footer class="tagline-band">
    <p class="tagline">Your Health ,Your Responsibility</p>
  </footer>

</div>
</body>
</html>
```